KiteSurf Weather App Forecast Screen re-design (1 Screen)

We are redesigning our application, BreezeLoom. Our main screen is the forecast screen. The forecast screen presents the forecast for multiple places for the selected day.

Intro
-----

The user has a list of favorite spots that he is monitoring. Then he selects the date that he wants to get the forecast. The forecast screen presents a list of all the spots and a summary of the weather conditions. Spots are sorted by weather conditions. At the top, he gets the spot with the best weather conditions. We have an algorithm that can evaluate whether given weather conditions are good or not. When they are good we indicate that to the user.

Current Solution
------------------

There is also a landscape version, which contains a bit more data: "Current Forecast Screen Lanscape.jpeg". The landscape one is a bit funny, as it is taken from an Zentra Q and the app was not designed for it at the time.

The bars that you see for each hour use our algorithm to display whether the conditions are good:

- When the color is gray the conditions are not good
- When the color is yellow there are light wind conditions
- When the color is green there are good
- When the color is red the wind is very strong
- The height of the bar indicates wind strength

More Info
-----------

The detailed forecast screen is also attached so you can get a bit more context, "DetailedForecast.jpeg"

An example from an application that has a similar chart is attached, "SimilarApp.jpeg". I have circled the chart with red.

Future Solution
------------------

(See note.jpeg)

We want to create a page that contains more information and passes a better message to our users.

The elements that are important and we want to present to the user are the following:

1. Wind. (The most important)
It contains two elements: strength and direction.

1.1 Wind Strength.
Good wind strength is anything between 10-45 knots (measurement unit like km/h). The best representation with a color palette.
Gray will be the color used when the strength is not between 10-45.
The palette should start with yellow at 10 knots, then move toward green for 22knots and finally go towards red for 45 knots.

1.2 Wind Direction.
There are good wind directions that we can kite and directions that is is not possible.
Can be presented by an arrow that points in the direction the wind is blowing to. The color of the arrow will be green when the direction is good, yellow when it is average and gray when it is not good.

My thought for portrait mode is to use an arrow point for the direction and the color of the arrow to represent the strength. Solution number 2 on my notes. Then for landscape, we could use both a number and an arrow like number 4 on my notes.

2. Wave.
It contains three elements: height, period and direction. It is not displayed to all of our users only the ones that have selected the wave riding option.

2.1 Height is represented by a number. Ex. 1.2 meters or 2 foot.
2.2 Period is represented in seconds. Ex. 12 seconds.
2.3 Directions is an arrow that points to the direction the wave is coming from.

Again the solution should be like the wind. Arrow for direction and the color of the arrow for height. The palette here should be something with different blue colors.

3. Tide height. (Optional for tidal spots, as not all spots have tides)

The best way to represent that it through a graph. I would also like to see an alternative, where we have three symbols for low, mid and high tide.

4. General Weather. Rain/Snow and temperature.

This should be represented by a sun/cloud/rain symbol. If it is very cold the symbol can also contain an ice sign on the background.

---------

This is a guideline creativity will be valued. Maybe there is another way to do it that I have not thought about.

The winner of the competition will have to send us all graphics used in vector format, so we can input them to our xCode project.

Finally the person that wins the competition will be the first one to be considered for the redesign of the rest of our application.

Target Market(s)

Kitesurfers

Font styles to use
Sans Serif

Colors

Designer to choose colors to be used in the design.

Requirements
Must have
• It should be minimal and clearly communicate the weather forecast to my users. It should be user friendly.
Nice to have
• Communicative color palettes for both wind strength, tide and waves
Should not have
• Hard to understand UI

```html
<!DOCTYPE html>
<html lang="en">
<head>
<meta charset="utf-8">
<title>BreezeLoom – Main Screen</title>
<link href="https://fonts.googleapis.com/css2?family=Roboto:wght@400;500;700&display=swap" rel="stylesheet">
<style>
  :root{
    --bg:#ececec;
    --navy:#0b2233;
    --grey:#474c52;
    --accent:#1586b8;
    --ink:#222;
    --green:#2dbb4c;
    --red:#d8262c;
    --orange:#f5a300;
    --arrow-blue:#2f6fe0;
    --arrow-navy:#1a3a8c;
    --bar-blue:#2b7fe3;
    --bar-navy:#1c3cb8;
    --bar-purple:#6b2bc1;
    --line:#e4e6ea;
  }
  *{box-sizing:border-box;margin:0;padding:0}
  html,body{width:1200px;height:1200px;overflow:hidden}
  body{background:var(--bg);font-family:"Roboto",Arial,sans-serif;color:var(--ink);position:relative}

  /* ---------- app screen ---------- */
  .screen{position:absolute;left:140px;top:160px;width:462px;height:821px;background:#fff;overflow:hidden;box-shadow:0 10px 40px rgba(0,0,0,.12)}
  .status-bar{height:26px;display:flex;align-items:center;justify-content:space-between;padding:0 8px;font-size:13px;font-weight:500}
  .status-bar .battery{display:inline-block;width:28px;height:11px;border:1px solid #222;border-radius:2px;padding:1px;vertical-align:middle}
  .status-bar .battery i{display:block;height:100%;background:#222}
  .app-header{height:52px;display:flex;align-items:center;justify-content:space-between;padding:0 14px}
  .app-header h1{font-size:19px;font-weight:500}
  .hours{height:56px;display:flex;align-items:center;padding:0 13px 0 23px;border-bottom:1px solid var(--line);background:#fafafa}
  .hours ol{display:flex;list-style:none;margin-left:27px}
  .hours li{width:48px;text-align:center;font-size:15px;color:#333}

  .spots{padding:8px 13px 0;background:#f3f4f6;height:535px}
  .spot{background:#fff;border-radius:4px;margin-bottom:13px;box-shadow:0 1px 4px rgba(0,0,0,.15);overflow:hidden}
  .spot-head{height:83px;padding:10px 12px 0;color:#fff;background:var(--navy)}
  .spot.poor .spot-head{background:var(--grey)}
  .spot-title{display:flex;justify-content:space-between;font-size:19px}
  .spot-title span{font-size:17px}
  .spot-summary{display:grid;grid-template-columns:128px repeat(4,85px);align-items:center;margin-top:6px}
  .badge{display:inline-block;width:74px;height:27px;border-radius:14px;font-size:15px;text-align:center;line-height:27px}
  .badge.good{background:var(--green)}
  .badge.poor{background:var(--red)}
  .spot-summary svg{width:36px;height:30px}

  .row{display:grid;grid-template-columns:40px repeat(8,48px);align-items:center;padding-left:10px;border-bottom:1px solid var(--line)}
  .row:last-child{border-bottom:0}
  .row .ico{width:26px;height:26px;display:block}
  .wind-row{height:48px}
  .wave-row{height:52px}
  .cell{text-align:center;font-size:13px;line-height:1.15;white-space:nowrap}
  .cell svg{width:14px;height:15px;display:block;margin:0 auto 3px}
  .wave-row .cell{font-size:11.5px;color:#444}
  .c-green{color:var(--green)} .c-red{color:var(--red)} .c-yellow{color:var(--orange)} .c-grey{color:#666}
  .c-blue{color:var(--arrow-blue)} .c-navy{color:var(--arrow-navy)}
  .cell b{font-weight:400}

  .bars-row{height:42px}
  .bars{grid-column:2 / span 8;display:flex;align-items:flex-end;justify-content:space-between;height:28px;padding:0 6px}
  .bars i{display:block;width:5px;border-radius:3px;background:var(--bar-blue)}
  .bars i.n{background:var(--bar-navy)} .bars i.p{background:var(--bar-purple)}

  .tab-bar{position:absolute;left:0;right:0;bottom:0;height:64px;background:#fff;border-top:1px solid var(--line);display:flex;align-items:center;overflow:hidden}
  .tab-bar ul{display:flex;list-style:none;margin-left:-36px}
  .tab-bar li{width:61.5px;text-align:center;font-size:15px;color:#555;position:relative}
  .tab-bar li.active{color:var(--accent)}
  .tab-bar li.active::before{content:"";position:absolute;left:14px;right:14px;top:-11px;height:3px;background:var(--accent)}
  .tab-bar .mark{display:block;margin:6px auto 0;width:17px;height:17px;border-radius:50%;background:#555;color:#fff;font-size:11px;line-height:17px}
  .tab-bar li.active .mark{background:var(--accent)}
  .tab-bar .lock{display:block;margin:6px auto 0;width:14px;height:17px}

  /* ---------- presentation ---------- */
  .title-pill{position:absolute;left:668px;top:80px;width:452px;height:88px;border:3px solid var(--accent);border-radius:44px;display:flex;align-items:center;justify-content:center;font-size:36px;font-weight:700;letter-spacing:2px;color:var(--accent)}
  .connectors{position:absolute;left:0;top:0;width:1200px;height:1200px;pointer-events:none}
  .note{position:absolute;left:810px;width:360px}
  .note h2{font-size:23px;font-weight:700;color:var(--accent);letter-spacing:.5px;margin-bottom:10px}
  .note p{font-size:21px;line-height:1.2;color:#333}
  .note strong{color:#111}
  .note.good{top:316px}
  .note.poor{top:656px}
</style>
</head>
<body>

<svg width="0" height="0" style="position:absolute">
  <defs>
    <symbol id="arrow" viewBox="0 0 12 14"><polygon points="6,0 12,14 6,10 0,14" fill="currentColor"/></symbol>
    <symbol id="ico-wind" viewBox="0 0 26 26"><circle cx="13" cy="13" r="13" fill="#0b2233"/><path d="M6 10h11a2.5 2.5 0 1 0-2.5-2.5M5 14h15a2.5 2.5 0 1 1-2.5 2.5M8 18h5" stroke="#fff" stroke-width="1.6" fill="none" stroke-linecap="round"/></symbol>
    <symbol id="ico-wave" viewBox="0 0 26 26"><circle cx="13" cy="13" r="13" fill="#0b2233"/><path d="M5 18c3 0 4-2 5-5s3-5 7-5c2 0 3 1 4 2c-3-1-6 1-5 4c1 2 3 3 5 3c-1 1-2 1-3 1z" fill="#fff"/></symbol>
    <symbol id="ico-tide" viewBox="0 0 26 26"><circle cx="13" cy="13" r="13" fill="#0b2233"/><path d="M6 9c2-2 3 2 5 0s3 2 5 0s3 2 5 0M6 13c2-2 3 2 5 0s3 2 5 0s3 2 5 0M6 17c2-2 3 2 5 0s3 2 5 0s3 2 5 0" stroke="#fff" stroke-width="1.4" fill="none"/></symbol>
    <symbol id="cloud" viewBox="0 0 36 30"><circle cx="24" cy="10" r="6" fill="#f7b500"/><path d="M6 24a6 6 0 0 1 2-11.6A8 8 0 0 1 23 12a6 6 0 0 1 5 12z" fill="#fff"/></symbol>
    <symbol id="fog" viewBox="0 0 36 30"><path d="M7 18a6 6 0 0 1 2-11.6A8 8 0 0 1 24 6a6 6 0 0 1 5 12z" fill="#fff"/><rect x="6" y="21" width="24" height="2" fill="#6cc4f0"/><rect x="10" y="26" width="18" height="2" fill="#6cc4f0"/></symbol>
    <symbol id="wind" viewBox="0 0 36 30"><path d="M4 12h22a3 3 0 1 0-3-3M2 17h28a3 3 0 1 1-3 3M8 22h10" stroke="#4bb6ee" stroke-width="2" fill="none" stroke-linecap="round"/></symbol>
    <symbol id="sunwind" viewBox="0 0 36 30"><circle cx="14" cy="15" r="9" fill="#f7b500"/><path d="M16 12h16M18 16h14M16 20h12" stroke="#fff" stroke-width="2"/></symbol>
    <symbol id="rain" viewBox="0 0 36 30"><path d="M7 16a6 6 0 0 1 2-11.6A8 8 0 0 1 24 4a6 6 0 0 1 5 12z" fill="#fff"/><path d="M10 20l-2 6M15 20l-2 6M20 20l-2 6M25 20l-2 6" stroke="#6cc4f0" stroke-width="1.6"/></symbol>
    <symbol id="storm" viewBox="0 0 36 30"><path d="M7 16a6 6 0 0 1 2-11.6A8 8 0 0 1 24 4a6 6 0 0 1 5 12z" fill="#fff"/><path d="M11 19l-2 6M16 19l-2 6" stroke="#6cc4f0" stroke-width="1.6"/><polygon points="22,17 18,24 21,24 19,30 26,21 23,21 25,17" fill="#f7b500"/></symbol>
    <symbol id="windrain" viewBox="0 0 36 30"><path d="M4 12h22a3 3 0 1 0-3-3M2 17h28a3 3 0 1 1-3 3" stroke="#4bb6ee" stroke-width="2" fill="none" stroke-linecap="round"/><path d="M8 22l-1 3M13 22l-1 3M18 22l-1 3" stroke="#fff" stroke-width="1.4"/></symbol>
    <symbol id="suncloudstorm" viewBox="0 0 36 30"><circle cx="24" cy="9" r="6" fill="#f7b500"/><path d="M6 22a6 6 0 0 1 2-11.6A8 8 0 0 1 23 10a6 6 0 0 1 5 12z" fill="#fff"/><polygon points="15,20 11,26 14,26 12,30 19,24 16,24 18,20" fill="#f7b500"/></symbol>
    <symbol id="lock" viewBox="0 0 14 17"><path d="M3 7V5a4 4 0 0 1 8 0v2" stroke="#555" stroke-width="2" fill="none"/><rect x="0" y="7" width="14" height="10" rx="2" fill="#555"/></symbol>
  </defs>
</svg>

<main class="screen">
  <div class="status-bar">
    <span>▮▮▮ Norvia</span><span>9:41 AM</span><span>100% <span class="battery"><i></i></span></span>
  </div>

  <header class="app-header">
    <svg width="32" height="22" viewBox="0 0 32 22" aria-label="Menu"><path d="M2 4h6M6 9h22M2 14h26M8 19h16" stroke="var(--accent)" stroke-width="2.6" stroke-linecap="round"/></svg>
    <h1>Thursday, 28 December</h1>
    <svg width="30" height="22" viewBox="0 0 30 22" aria-label="Filter"><polygon points="0,1 16,1 10,10 10,20 6,17 6,10" fill="var(--accent)"/><path d="M19 5h10M19 11h10M19 17h10" stroke="var(--accent)" stroke-width="2.4"/></svg>
  </header>

  <nav class="hours">
    <svg width="24" height="24" viewBox="0 0 24 24" aria-label="Time"><circle cx="12" cy="12" r="12" fill="var(--navy)"/><path d="M12 5v7h6" stroke="#fff" stroke-width="2.2" fill="none"/></svg>
    <ol><li>06h</li><li>07h</li><li>08h</li><li>09h</li><li>10h</li><li>11h</li><li>12h</li><li>13h</li></ol>
  </nav>

  <section class="spots">
    <article class="spot good">
      <div class="spot-head">
        <div class="spot-title">Harlow Point Park<span>70 km</span></div>
        <div class="spot-summary">
          <span class="badge good">GOOD</span>
          <svg><use href="#cloud"/></svg><svg><use href="#fog"/></svg><svg><use href="#wind"/></svg><svg><use href="#sunwind"/></svg>
        </div>
      </div>
      <div class="row wind-row">
        <svg class="ico" aria-label="Wind"><use href="#ico-wind"/></svg>
        <div class="cell c-green"><svg style="transform:rotate(45deg)"><use href="#arrow"/></svg>20</div>
        <div class="cell c-green"><svg style="transform:rotate(45deg)"><use href="#arrow"/></svg><b class="c-red">32</b></div>
        <div class="cell c-yellow"><svg style="transform:rotate(160deg)"><use href="#arrow"/></svg><b class="c-red">29</b></div>
        <div class="cell c-yellow"><svg style="transform:rotate(100deg)"><use href="#arrow"/></svg><b class="c-grey">10</b></div>
        <div class="cell c-yellow"><svg style="transform:rotate(100deg)"><use href="#arrow"/></svg>12</div>
        <div class="cell c-green"><svg style="transform:rotate(110deg)"><use href="#arrow"/></svg>26</div>
        <div class="cell c-green"><svg style="transform:rotate(45deg)"><use href="#arrow"/></svg>28</div>
        <div class="cell c-yellow"><svg style="transform:rotate(-20deg)"><use href="#arrow"/></svg>14</div>
      </div>
      <div class="row wave-row">
        <svg class="ico" aria-label="Wave"><use href="#ico-wave"/></svg>
        <div class="cell"><svg class="c-blue" style="transform:rotate(30deg)"><use href="#arrow"/></svg>0.3ᵐ<br>9.8ˢ</div>
        <div class="cell"><svg class="c-blue" style="transform:rotate(30deg)"><use href="#arrow"/></svg>0.4ᵐ<br>9.9ˢ</div>
        <div class="cell"><svg class="c-blue" style="transform:rotate(-60deg)"><use href="#arrow"/></svg>0.5ᵐ<br>10.0ˢ</div>
        <div class="cell"><svg class="c-navy" style="transform:rotate(-80deg)"><use href="#arrow"/></svg>0.6ᵐ<br>9.9ˢ</div>
        <div class="cell"><svg class="c-navy" style="transform:rotate(-80deg)"><use href="#arrow"/></svg>0.7ᵐ<br>9.8ˢ</div>
        <div class="cell"><svg class="c-navy" style="transform:rotate(180deg)"><use href="#arrow"/></svg>0.8ᵐ<br>10.1ˢ</div>
        <div class="cell"><svg class="c-navy" style="transform:rotate(160deg)"><use href="#arrow"/></svg>0.9ᵐ<br>11.2ˢ</div>
        <div class="cell"><svg class="c-navy" style="transform:rotate(160deg)"><use href="#arrow"/></svg>1.0ᵐ<br>11.4ˢ</div>
      </div>
      <div class="row bars-row">
        <svg class="ico" aria-label="Tide"><use href="#ico-tide"/></svg>
        <div class="bars">
          <i style="height:10px"></i><i style="height:12px"></i><i class="n" style="height:16px"></i><i style="height:10px"></i><i class="n" style="height:16px"></i><i class="p" style="height:22px"></i><i class="p" style="height:26px"></i><i class="p" style="height:26px"></i><i class="p" style="height:22px"></i><i class="n" style="height:18px"></i><i class="n" style="height:20px"></i><i class="n" style="height:22px"></i><i class="p" style="height:24px"></i><i class="p" style="height:22px"></i><i class="n" style="height:16px"></i><i style="height:12px"></i><i style="height:8px"></i><i style="height:10px"></i><i style="height:12px"></i><i class="n" style="height:16px"></i><i style="height:12px"></i><i style="height:10px"></i><i class="n" style="height:16px"></i><i style="height:10px"></i><i style="height:12px"></i><i class="n" style="height:18px"></i><i class="p" style="height:24px"></i><i class="p" style="height:26px"></i><i class="p" style="height:22px"></i><i class="n" style="height:18px"></i>
        </div>
      </div>
    </article>

    <article class="spot poor">
      <div class="spot-head">
        <div class="spot-title">The Morning Breeze<span>8 km</span></div>
        <div class="spot-summary">
          <span class="badge poor">POOR</span>
          <svg><use href="#windrain"/></svg><svg><use href="#rain"/></svg><svg><use href="#storm"/></svg><svg><use href="#suncloudstorm"/></svg>
        </div>
      </div>
      <div class="row wind-row">
        <svg class="ico" aria-label="Wind"><use href="#ico-wind"/></svg>
        <div class="cell c-grey"><svg style="transform:rotate(45deg)"><use href="#arrow"/></svg><b class="c-yellow">14</b></div>
        <div class="cell c-grey"><svg style="transform:rotate(20deg)"><use href="#arrow"/></svg><b class="c-green">22</b></div>
        <div class="cell c-grey"><svg style="transform:rotate(-60deg)"><use href="#arrow"/></svg><b class="c-green">19</b></div>
        <div class="cell c-yellow"><svg style="transform:rotate(-90deg)"><use href="#arrow"/></svg><b class="c-grey">8</b></div>
        <div class="cell c-yellow"><svg style="transform:rotate(-90deg)"><use href="#arrow"/></svg><b class="c-grey">10</b></div>
        <div class="cell c-yellow"><svg style="transform:rotate(180deg)"><use href="#arrow"/></svg>13</div>
        <div class="cell c-green"><svg style="transform:rotate(135deg)"><use href="#arrow"/></svg><b class="c-red">29</b></div>
        <div class="cell c-green"><svg style="transform:rotate(135deg)"><use href="#arrow"/></svg><b class="c-red">30</b></div>
      </div>
      <div class="row bars-row">
        <svg class="ico" aria-label="Tide"><use href="#ico-tide"/></svg>
        <div class="bars">
          <i class="n" style="height:20px"></i><i class="p" style="height:24px"></i><i class="p" style="height:26px"></i><i class="n" style="height:22px"></i><i style="height:14px"></i><i style="height:8px"></i><i style="height:12px"></i><i class="n" style="height:16px"></i><i style="height:10px"></i><i style="height:12px"></i><i class="n" style="height:16px"></i><i style="height:10px"></i><i style="height:8px"></i><i class="n" style="height:14px"></i><i class="n" style="height:16px"></i><i class="n" style="height:18px"></i><i class="p" style="height:22px"></i><i class="p" style="height:24px"></i><i class="n" style="height:20px"></i><i class="n" style="height:18px"></i><i class="n" style="height:20px"></i><i class="p" style="height:22px"></i><i class="p" style="height:26px"></i><i class="p" style="height:24px"></i><i class="n" style="height:18px"></i><i class="n" style="height:16px"></i><i style="height:10px"></i><i style="height:14px"></i><i style="height:12px"></i><i style="height:12px"></i>
        </div>
      </div>
    </article>

    <article class="spot good">
      <div class="spot-head">
        <div class="spot-title">Xavier Heights<span>4 km</span></div>
        <div class="spot-summary">
          <span class="badge good">GOOD</span>
          <svg><use href="#cloud"/></svg><svg><use href="#wind"/></svg><svg><use href="#fog"/></svg><svg><use href="#sunwind"/></svg>
        </div>
      </div>
      <div class="row wind-row">
        <svg class="ico" aria-label="Wind"><use href="#ico-wind"/></svg>
        <div class="cell c-green"><svg style="transform:rotate(45deg)"><use href="#arrow"/></svg>19</div>
        <div class="cell c-green"><svg style="transform:rotate(45deg)"><use href="#arrow"/></svg><b class="c-red">30</b></div>
        <div class="cell c-yellow"><svg style="transform:rotate(160deg)"><use href="#arrow"/></svg>16</div>
        <div class="cell c-yellow"><svg style="transform:rotate(100deg)"><use href="#arrow"/></svg><b class="c-grey">8</b></div>
        <div class="cell c-yellow"><svg style="transform:rotate(100deg)"><use href="#arrow"/></svg>13</div>
        <div class="cell c-green"><svg style="transform:rotate(110deg)"><use href="#arrow"/></svg>28</div>
        <div class="cell c-green"><svg style="transform:rotate(45deg)"><use href="#arrow"/></svg>22</div>
        <div class="cell c-yellow"><svg style="transform:rotate(-20deg)"><use href="#arrow"/></svg>14</div>
      </div>
      <div class="row bars-row">
        <svg class="ico" aria-label="Tide"><use href="#ico-tide"/></svg>
        <div class="bars">
          <i style="height:10px"></i><i style="height:12px"></i><i class="n" style="height:16px"></i><i style="height:10px"></i><i class="n" style="height:16px"></i><i class="p" style="height:22px"></i><i class="p" style="height:26px"></i><i class="p" style="height:26px"></i><i class="p" style="height:22px"></i><i class="n" style="height:18px"></i><i class="n" style="height:20px"></i><i class="n" style="height:22px"></i><i class="p" style="height:24px"></i><i class="p" style="height:22px"></i><i class="n" style="height:16px"></i><i style="height:12px"></i><i style="height:8px"></i><i style="height:10px"></i><i style="height:12px"></i><i class="n" style="height:16px"></i><i style="height:12px"></i><i style="height:10px"></i><i class="n" style="height:16px"></i><i style="height:10px"></i><i style="height:12px"></i><i class="n" style="height:18px"></i><i class="p" style="height:24px"></i><i class="p" style="height:26px"></i><i class="p" style="height:22px"></i><i class="n" style="height:18px"></i>
        </div>
      </div>
    </article>
  </section>

  <footer class="tab-bar">
    <ul>
      <li>WE<svg class="lock"><use href="#lock"/></svg></li>
      <li>TUE<svg class="lock"><use href="#lock"/></svg></li>
      <li>WED<span class="mark">0</span></li>
      <li class="active">THU<span class="mark">4</span></li>
      <li>FRI<span class="mark">2</span></li>
      <li>SAT<svg class="lock"><use href="#lock"/></svg></li>
      <li>SUN<svg class="lock"><use href="#lock"/></svg></li>
      <li>MO<svg class="lock"><use href="#lock"/></svg></li>
    </ul>
  </footer>
</main>

<div class="title-pill">MAIN SCREEN</div>

<svg class="connectors" viewBox="0 0 1200 1200">
  <g stroke="var(--accent)" stroke-width="2" fill="none">
    <path d="M579 348H790"/>
    <path d="M579 603H790V672"/>
  </g>
  <g fill="var(--accent)">
    <circle cx="579" cy="348" r="5" fill="#fff" stroke="var(--accent)" stroke-width="2"/>
    <circle cx="790" cy="348" r="5"/>
    <circle cx="579" cy="603" r="5" fill="#fff" stroke="var(--accent)" stroke-width="2"/>
    <circle cx="790" cy="672" r="5"/>
  </g>
</svg>

<div class="note good">
  <h2>GOOD WEATHER</h2>
  <p>Card header would be in <strong>dark blue color</strong> which indicates the weather is good.</p>
</div>

<div class="note poor">
  <h2>POOR WEATHER</h2>
  <p>Card header would be in <strong>grey color</strong> indicating a poor / bad weather.</p>
</div>

</body>
</html>
```